Web Design Project

The client is unsure if they want a completely new design or a design that matches their existing site closely (https://www.talvoinsurance.com.au). So essentially we are looking for some designs that reflect the existing sites shape and colour and some designs that have their own new style. The company will sell three main types of insurance, Car, Bike and Caravan.

Read the complete brief and in the attached document.
The logo is also attached

I have also attached a zip of a few classic cars, if you can incorporate those.

Industry/Entity Type

Insurance

Requirements
Should not have

```html
<!DOCTYPE html>
<html lang="en">
<head>
<meta charset="utf-8">
<title>Talvo Insurance — Classic and Prestige Car and Bike Insurance</title>
<link href="https://fonts.googleapis.com/css2?family=Maven+Pro:wght@400;500;600&family=Open+Sans:wght@400;600;700&display=swap" rel="stylesheet">
<style>
:root{
  --orange:#e8590c;
  --orange-light:#f07a2e;
  --orange-dark:#b83f05;
  --red-band:#8a1d0a;
  --charcoal:#3d3d3d;
  --charcoal-dark:#2b2b2b;
  --slate:#5a5a5a;
  --slate-dark:#3a3a3a;
  --blue:#2a9ad6;
  --blue-dark:#1b6f9e;
  --white:#ffffff;
  --page:#e9e9e9;
  --ink:#222222;
  --muted:#555555;
}
*{box-sizing:border-box;margin:0;padding:0}
html,body{width:1200px;height:1095px;overflow:hidden}
body{position:relative;font-family:"Open Sans",Arial,sans-serif;color:var(--ink);
  background:linear-gradient(90deg,#dcdcdc 0%,#f6f6f6 30%,#f6f6f6 70%,#dcdcdc 100%)}
.abs{position:absolute}
a{color:inherit;text-decoration:none}

/* utility bar */
.utility{top:0;left:0;width:1200px;height:35px;background:linear-gradient(#fafafa,#ececec)}
.utility ul{position:absolute;right:208px;top:10px;display:flex;gap:26px;list-style:none;
  font-family:"Maven Pro",sans-serif;font-size:11.5px;font-weight:600;color:#555;letter-spacing:.3px}
.utility li{display:flex;align-items:center;gap:6px}
.utility .ico{color:var(--orange);font-weight:700}

/* navigation band */
.nav-band{top:35px;left:0;width:1200px;height:50px;background:var(--orange)}
.brand{top:32px;left:238px;width:150px;height:60px;display:flex;align-items:center;gap:8px;
  font-family:"Open Sans",sans-serif;font-weight:700;font-size:19px;color:var(--white);letter-spacing:.5px}
.brand .mark{width:14px;height:14px;border-radius:50%;background:var(--white);flex:none}
.main-nav{top:49px;left:477px;display:flex;list-style:none;font-family:"Maven Pro",sans-serif;
  font-size:12px;font-weight:600;color:var(--white);letter-spacing:.3px}
.main-nav li{height:23px;line-height:23px;padding:0 11px;border-right:1px solid rgba(255,255,255,.35)}
.main-nav li:last-child{border-right:0}
.main-nav li.active{background:var(--white);color:var(--ink);width:79px;text-align:center}
.dropdown{top:75px;left:477px;width:132px;background:#fff;padding:4px;box-shadow:0 2px 4px rgba(0,0,0,.3);z-index:5}
.dropdown li{list-style:none;background:var(--charcoal);color:#fff;font-size:11px;height:22px;line-height:22px;padding-left:6px;margin-bottom:3px}
.dropdown li:last-child{margin-bottom:0}

/* hero */
.hero-top{top:85px;left:0;width:1200px;height:73px;background:linear-gradient(90deg,#d6d6d6,#f4f4f4 30%,#f4f4f4 70%,#d6d6d6)}
.hero-band{top:158px;left:0;width:1200px;height:158px;background:linear-gradient(90deg,var(--orange-dark),var(--orange) 40%,var(--orange-light) 60%,var(--orange-dark))}
.hero-copy{top:98px;left:326px;width:220px;text-align:center;font-size:14px;color:var(--ink);line-height:18px}
.hero-copy .tag{font-size:11px;font-weight:600;margin-top:4px}
.hero-car{top:85px;left:584px;width:311px;height:200px;border-radius:45% 50% 30% 30%;
  background:radial-gradient(ellipse at 50% 45%,#a3202a 0%,#7a1520 55%,rgba(90,20,20,0) 72%)}
.quote-btn{top:202px;left:225px;width:169px;height:39px;border-radius:6px;
  background:linear-gradient(#fff3ea,#f6c9a6);box-shadow:0 2px 3px rgba(0,0,0,.35);
  font-family:"Maven Pro",sans-serif;font-weight:600;font-size:15px;color:#333;text-align:center;line-height:39px;letter-spacing:.3px}

/* main panel */
.panel{top:286px;left:225px;width:750px;height:667px;background:var(--charcoal)}
.card-tray{top:296px;left:237px;width:728px;height:190px;background:var(--white)}
.card{top:307px;width:227px;height:168px;color:#fff;font-size:9.2px;line-height:12px}
.card h3{height:34px;line-height:34px;padding-left:14px;font-family:"Maven Pro",sans-serif;font-weight:500;font-size:16px;letter-spacing:.5px}
.card p{padding:8px 16px 0 16px}
.card.car{left:249px;background:var(--orange)}
.card.car h3{background:var(--red-band)}
.card.bike{left:488px;background:var(--slate)}
.card.bike h3,.card.benefits h3{background:var(--slate-dark)}
.card.benefits{left:727px;background:var(--slate)}
.card.benefits ul{list-style:none;padding:6px 16px 0 24px;font-size:8.6px;line-height:10.6px}
.card.benefits li::before{content:"›";margin-right:4px}
.more{position:absolute;right:0;bottom:0;height:20px;width:72px;font-size:10px;font-weight:700;
  line-height:20px;text-align:right;padding-right:8px;letter-spacing:.3px}
.more::before{content:"";position:absolute;left:0;top:0;border-style:solid;border-width:0 0 20px 14px;border-color:transparent transparent currentColor transparent}
.card.car .more{background:var(--white);color:var(--slate);}
.card.car .more::before{color:var(--white);left:-14px}
.card.bike .more,.card.benefits .more{background:var(--charcoal-dark);color:#fff}
.card.bike .more::before,.card.benefits .more::before{color:var(--charcoal-dark);left:-14px}

.intro{top:497px;left:237px;width:728px;height:90px;border:1px solid #555;
  background:linear-gradient(#5b5b5b,#3d3d3d);padding:8px 12px;color:#fff}
.intro h2{font-family:"Maven Pro",sans-serif;font-weight:400;font-size:20px;margin-bottom:6px}
.intro p{font-size:10px;line-height:14px}

.section-head{height:27px;line-height:27px;background:var(--charcoal-dark);color:#fff;padding-left:12px;
  font-family:"Maven Pro",sans-serif;font-size:13px;letter-spacing:.4px}
.news-head{top:596px;left:237px;width:423px}
.news{top:634px;left:237px;width:423px;height:156px;background:var(--white)}
.news-photo{position:absolute;top:9px;left:12px;width:207px;height:137px;background:linear-gradient(135deg,#c8b8a6,#6a5e54)}
.news-body{position:absolute;top:10px;left:233px;width:178px;font-size:9.3px;line-height:12.3px}
.news-body h4{font-weight:400;font-size:11.5px;margin-bottom:10px}
.news-body .more-info{display:block;text-align:right;margin-top:10px;font-size:9px}

.social{top:596px;left:677px;width:286px;height:191px;background:var(--blue)}
.social h3{height:33px;line-height:33px;padding-left:13px;color:#fff;font-family:"Maven Pro",sans-serif;font-weight:500;font-size:13px;letter-spacing:.4px}
.social-box{position:absolute;top:33px;left:12px;width:261px;height:149px;background:#fff;padding:6px 8px;font-size:8px;color:#444}
.social-box .row{display:flex;gap:8px;padding-bottom:8px;border-bottom:1px solid #9fc8df}
.social-box .avatar{width:40px;height:40px;background:#333}
.social-box strong{font-size:10px;color:#222;display:block;margin-bottom:4px}
.like{display:inline-block;border:1px solid #aaa;background:#eee;padding:1px 6px;font-size:9px;font-weight:600;color:#333}
.social-box .count{margin:8px 0 6px}
.social-box .count span{color:var(--blue-dark)}
.faces{display:flex;gap:5px}
.faces i{display:block;width:26px;height:24px;background:#2a2a2a}

.events-head{top:802px;left:237px;width:423px}
.event-banner{top:841px;left:237px;width:423px;height:96px;border:2px solid #222;
  background:linear-gradient(#c04a0e 0%,#8a3b22 30%,#4e2a6e 60%,#3b2266 100%)}

.faq{top:802px;left:677px;width:286px;height:135px;background:var(--blue);color:#fff}
.faq h3{height:34px;line-height:34px;padding-left:13px;font-family:"Maven Pro",sans-serif;font-weight:500;font-size:13px;letter-spacing:.4px}
.faq ul{list-style:none;padding-left:15px;font-size:10.5px;line-height:21.5px}
.faq li::before{content:"›";margin-right:8px;font-weight:700}
.faq .more{background:var(--blue-dark);color:#fff;width:68px;height:28px;line-height:28px;font-size:11px}
.faq .more::before{color:var(--blue-dark);left:-16px;border-width:0 0 28px 16px}

/* footer */
.footer{top:969px;left:0;width:1200px;height:107px;background:var(--orange);color:#fff}
.foot-col{position:absolute;top:11px;font-size:10.5px;line-height:15.5px}
.foot-col h5{font-family:"Maven Pro",sans-serif;font-size:11px;font-weight:600;margin-bottom:8px;letter-spacing:.3px}
.foot-col ul{list-style:none}
.foot-col li::before{content:"› "}
.nav-cols{display:flex;gap:40px}
.map{position:absolute;top:8px;left:807px;width:158px;height:90px;border:3px solid #444;background:linear-gradient(135deg,#eee6d4,#d8dccd)}
.copyright{top:1076px;left:0;width:1200px;height:19px;background:#fff;text-align:center;font-size:9px;line-height:19px;color:#333}
</style>
</head>
<body>

<header>
  <div class="abs utility">
    <ul>
      <li><span class="ico">$</span>MAKE A PAYMENT</li>
      <li><span class="ico">●</span>BROKER LOGIN</li>
      <li><span class="ico">♙</span>REGISTER</li>
    </ul>
  </div>
  <div class="abs nav-band"></div>
  <a class="abs brand" href="https://www.talvoinsurance.com.au"><span class="mark"></span>TALVO INSURANCE</a>
  <ul class="abs main-nav">
    <li class="active">ABOUT US</li><li>INSURANCE</li><li>EVENTS</li><li>CLUBS</li><li>LINKS</li><li>FAQ</li><li>CONTACT US</li>
  </ul>
  <ul class="abs dropdown"><li>Terms of Conditions</li><li>Careers</li></ul>
</header>

<section class="hero">
  <div class="abs hero-top"></div>
  <div class="abs hero-band"></div>
  <div class="abs hero-copy">Insure With an ENTHUSIAST<br>1300 482 915<div class="tag">Classic and Prestige Car and Bike Insurance</div></div>
  <div class="abs hero-car" role="img" aria-label="Red classic sports coupe"></div>
  <a class="abs quote-btn" href="#">GET A FREE QUOTE</a>
</section>

<main>
  <div class="abs panel"></div>
  <div class="abs card-tray"></div>

  <article class="abs card car">
    <h3>CAR INSURANCE</h3>
    <p>Lorem Ipsum is simply dummy text of the printing and typesetting industry. Lorem Ipsum has been the industry's standard dummy text ever since the 1500s, when an unknown printer took a galley of type and scrambled it to make a type specimen book</p>
    <a class="more" href="#">MORE ›</a>
  </article>
  <article class="abs card bike">
    <h3>BIKE INSURANCE</h3>
    <p>Lorem Ipsum is simply dummy text of the printing and typesetting industry. Lorem Ipsum has been the industry's standard dummy text ever since the 1500s, when an unknown printer took a galley of type and scrambled it to make a type specimen book</p>
    <a class="more" href="#">MORE ›</a>
  </article>
  <article class="abs card benefits">
    <h3>POLICY BENEFITS</h3>
    <ul>
      <li>Agreed Value</li><li>New Replacement Vehicle in first 2 years</li><li>Choice of Repairer</li><li>Lifetime Guarantee for Repairs</li><li>Free Windscreen/Glass Benefit</li><li>Hire car following accident or theft</li><li>Flexible coverage</li><li>Pay Premiums by Instalments</li><li>Salvage retained by you on vehicles over 30 years</li>
    </ul>
    <a class="more" href="#">MORE ›</a>
  </article>

  <section class="abs intro">
    <h2>The specialised car insurance cover your Classic or Prestige car needs</h2>
    <p>Talvo Insurance shares your passion for classic cars, vintage cars, prestige cars and hot rods. Don't just trust your specialist vehicle insurance to a general insurance provider – we're specialists, we've only insured cars like yours and will cover your car like it's one of our own. Call today to find out how much more we can do for you.</p>
  </section>

  <h3 class="abs section-head news-head">NEWS ON ALL THINGS MOTORING</h3>
  <article class="abs news">
    <div class="news-photo" role="img" aria-label="Distressed driver sitting behind the wheel of a car"></div>
    <div class="news-body">
      <h4>News title will goes here!</h4>
      <p>Lorem Ipsum is simply dummy text of the printing and typesetting industry. Lorem Ipsum has been the industry's standard dummy text ever since the 1500s, when an unknown printer took a galley of type and scrambled it to make a type specimen book</p>
      <a class="more-info" href="#">More info ›</a>
    </div>
  </article>

  <section class="abs social">
    <h3>CAR INSURANCE ON CHATTERLY</h3>
    <div class="social-box">
      <div class="row">
        <div class="avatar"></div>
        <div><strong>Talvo Insurance Services Pty Ltd</strong><span class="like">Like</span></div>
      </div>
      <p class="count">101 people like <span>Talvo Insurance Services.</span></p>
      <div class="faces"><i></i><i></i><i></i><i></i><i></i></div>
    </div>
  </section>

  <h3 class="abs section-head events-head">UPCOMING EVENTS</h3>
  <div class="abs event-banner" role="img" aria-label="Event banner: Sunday 18th November 2012, entrants and exhibitors, gates open 5.30am"></div>

  <section class="abs faq">
    <h3>TOP FAQS</h3>
    <ul><li>Lorem Ipsum is simply dummy text</li><li>Lorem Ipsum is simply dummy text</li><li>Lorem Ipsum is simply dummy text</li></ul>
    <a class="more" href="#">MORE ›</a>
  </section>
</main>

<footer class="abs footer">
  <div class="foot-col" style="left:234px">
    <h5>NAVIGATION</h5>
    <div class="nav-cols">
      <ul><li>ABOUT US</li><li>INSURANCE</li><li>EVENTS</li><li>CLUBS</li></ul>
      <ul><li>LINKS</li><li>FAQ</li><li>CONTACT US</li><li>SITEMAP</li></ul>
    </div>
  </div>
  <div class="foot-col" style="left:450px">
    <h5>OFFICE ADDRESS</h5>
    <p>Talvo Insurance Services<br>42 Harlow Street<br>Brenton Vale Qld 4190</p>
  </div>
  <div class="foot-col" style="left:616px">
    <h5>CONTACT</h5>
    <p>Ph: 1300 482 915<br>Fx: 1300 482 916<br>admin@talvoinsurance.com.au</p>
  </div>
  <div class="map" role="img" aria-label="Street map showing the office location"></div>
</footer>
<div class="abs copyright">Copyright © 2013 Talvo Insurance Services Pty Ltd. All Rights Reserved.</div>

</body>
</html>
```